Webdesign/Updates

We would like a landing page for an online course for our educators. So a website with about 3 to 5 pages - Home, About US, Online course, blog, and Contact us. We have a wordpress site up using a template, but we are looking for something that connects more with our new logo.

Target Market(s)

Educators, workshop trainers/instructors, colleges, community schools, educational institutions, global organizations

Industry/Entity Type

Education

Contact Information for Business Card

Use the words below as place holders for the front:
Name
Title
Address line 1
Address line 2
Email
Phone
Website URL

--the back
Logo
1 short question, use "What do you 1234 about your program?"

Number of Pages Required

4 page

Requirements
Must have
• Home page
• Course Page
• Blog
• right side bar with social media content and invitation to subscribe to newsletter
• see logo colors in document
Nice to have
• Newsletter Page with graphic that can be on this page or page can be sent as a pdf via email or in an email.
Should not have
• Be better than attached description
• clean simple look but stylish

```html
<!DOCTYPE html>
<html lang="en">
<head>
<meta charset="utf-8">
<title>Eduvanta – The Ultimate Course Design Program</title>
<link href="https://fonts.googleapis.com/css2?family=Montserrat:wght@400;600;700;800&family=Nunito:wght@400;600;700&display=swap" rel="stylesheet">
<style>
:root{
  --blue:#1b9bd7;
  --blue-dark:#1486bd;
  --green:#8dc63f;
  --orange:#f15a2b;
  --ink:#222a33;
  --text:#555b61;
  --grey-bg:#f3f4f5;
  --white:#ffffff;
  --navy:#1f2a36;
}
*{box-sizing:border-box;margin:0;padding:0}
html,body{width:1200px;height:3586px;overflow:hidden}
body{font-family:"Nunito",sans-serif;color:var(--text);background:var(--white);position:relative}
h1,h2,h3,h4,.heading{font-family:"Montserrat",sans-serif}
.container{width:1000px;margin:0 auto;position:relative;height:100%}
a{color:inherit;text-decoration:none}

/* top bar */
.topbar{height:48px;background:var(--blue);color:var(--white);font-size:12px}
.topbar .container{display:flex;align-items:center}
.social-dots{display:flex;gap:10px;margin-left:38px}
.social-dots span{width:24px;height:24px;border-radius:50%;background:var(--white);opacity:.9;display:block}
.top-contact{margin-left:auto;display:flex;gap:34px;align-items:center}
.top-contact span{display:flex;align-items:center;gap:7px}
.lang{background:var(--blue-dark);height:48px;padding:0 22px;display:flex;align-items:center;margin-left:24px;margin-right:-100px;letter-spacing:.5px}

/* header */
.header{height:76px;background:var(--white)}
.header .container{display:flex;align-items:center}
.brand{display:flex;align-items:center;gap:10px;margin-left:0}
.brand-square{width:38px;height:38px;background:var(--green);border-radius:4px}
.brand-name{font-family:"Montserrat",sans-serif;font-weight:800;font-size:28px;color:var(--navy);letter-spacing:.5px}
.header-info{margin-left:auto;display:flex;gap:60px;font-size:13px;color:var(--text)}
.header-info strong{display:block;color:var(--ink);font-size:15px;font-weight:700}
.login{margin-left:52px;border:1px solid #c9ced3;border-radius:18px;padding:7px 14px;font-size:12px;color:var(--ink);display:flex;align-items:center;gap:6px;font-weight:600}

/* nav */
.nav{height:44px;background:var(--green)}
.nav .container{display:flex;align-items:center}
.nav ul{list-style:none;display:flex;gap:46px;font-family:"Montserrat",sans-serif;font-weight:600;color:var(--white);font-size:14px}
.nav .search{margin-left:auto}

/* hero */
.hero{height:585px;position:relative;overflow:hidden}
.hero-photo{position:absolute;inset:0;background:linear-gradient(100deg,#2b2f33 0%,#4a4746 35%,#8a7060 60%,#b58d72 80%,#6c5a50 100%)}
.hero-shade{position:absolute;inset:0;background:linear-gradient(90deg,rgba(20,20,20,.55) 0%,rgba(20,20,20,.25) 55%,rgba(0,0,0,0) 100%)}
.hero-frame{position:absolute;left:96px;top:107px;width:286px;height:310px;border:6px solid rgba(200,200,200,.85);border-right:none}
.hero-frame::after{content:"";position:absolute;right:0;top:-6px;width:6px;height:48px;background:rgba(200,200,200,.85)}
.hero-frame::before{content:"";position:absolute;right:0;bottom:-6px;width:6px;height:48px;background:rgba(200,200,200,.85)}
.hero-copy{position:absolute;left:96px;top:183px;width:480px;color:var(--white)}
.hero-kicker{font-family:"Montserrat",sans-serif;font-weight:700;font-size:22px;letter-spacing:.5px}
.hero-title{font-family:"Montserrat",sans-serif;font-weight:800;font-size:48px;line-height:1.15;margin-top:6px;letter-spacing:.5px}
.hero-title .b{color:var(--blue)}
.hero-title .o{color:var(--orange)}
.hero-copy p{font-size:15px;line-height:1.5;margin-top:14px;width:420px}
.btn{display:inline-flex;align-items:center;gap:10px;background:var(--orange);color:var(--white);font-family:"Montserrat",sans-serif;font-weight:600;font-size:13px;padding:11px 20px}
.hero .btn{margin-top:28px;margin-left:-2px}
.hero-dots{position:absolute;left:100px;top:505px;display:flex;gap:8px}
.hero-dots span{width:30px;height:30px;border-radius:50%;background:var(--white);display:flex;align-items:center;justify-content:center}
.hero-dots span.on{background:var(--green)}
.hero-notch{position:absolute;left:50%;bottom:-1px;transform:translateX(-50%)}

/* intro */
.intro{height:562px}
.welcome{position:absolute;left:22px;top:88px;display:flex;align-items:center}
.welcome span{border:1px solid var(--green);color:var(--green);font-size:11px;padding:4px 10px;letter-spacing:.5px;font-weight:700}
.welcome i{display:block;width:48px;height:1px;background:var(--green)}
.intro-title{position:absolute;left:22px;top:133px;color:var(--orange);font-weight:800;font-size:32px;line-height:1.15}
.intro-sub{position:absolute;left:22px;top:215px;color:var(--ink);font-family:"Montserrat",sans-serif;font-weight:700;font-size:14px}
.intro-text{position:absolute;left:22px;top:262px;width:478px;font-size:15px;line-height:1.62}
.intro-actions{position:absolute;left:22px;top:466px;display:flex;align-items:center;gap:64px}
.intro-actions .btn{padding:12px 24px;gap:26px}
.phone{display:flex;align-items:center;gap:14px;font-size:17px;color:var(--ink);font-weight:600}
.phone i{width:40px;height:40px;border-radius:50%;background:var(--green);display:flex;align-items:center;justify-content:center}
.intro-media{position:absolute;left:536px;top:79px;width:435px;height:431px;display:grid;grid-template-columns:1fr 1fr;grid-template-rows:1fr 1fr;gap:3px}
.intro-media div{background:linear-gradient(135deg,#9a9a9a,#5f5f5f)}
.intro-media div:nth-child(2){background:linear-gradient(135deg,#d8d8d8,#8a8a8a)}
.intro-media div:nth-child(3){background:linear-gradient(135deg,#7a7a7a,#4c4c4c)}
.intro-media div:nth-child(4){background:linear-gradient(135deg,#bdbdbd,#707070)}
.video-box{position:absolute;left:601px;top:240px;width:130px;height:96px;background:var(--white);display:flex;flex-direction:column;align-items:center;justify-content:center;gap:6px;color:var(--orange);font-size:13px;font-weight:600}

/* section headings */
.sec-head{text-align:center}
.sec-head h2{font-weight:800;font-size:31px;letter-spacing:.3px}
.sec-head p{font-family:"Montserrat",sans-serif;font-weight:600;font-size:14px;margin-top:4px}
.divider{display:flex;justify-content:center;align-items:center;gap:8px;margin-top:8px}
.divider i{display:block;width:60px;height:1px}
.divider b{font-size:11px;letter-spacing:2px}

/* features */
.features{height:478px}
.features .sec-head{padding-top:54px}
.features h2{color:var(--blue)}
.features .sec-head p{color:var(--ink)}
.features .divider i{background:var(--blue)}
.features .divider b{color:var(--blue)}
.feature-grid{position:absolute;left:0;top:192px;display:grid;grid-template-columns:500px 500px;row-gap:44px}
.feature{display:flex;gap:22px}
.f-icon{width:90px;height:90px;border-radius:50%;flex:none;display:flex;align-items:center;justify-content:center}
.feature h3{font-weight:700;font-size:19px;color:var(--ink);margin-top:4px}
.feature p{font-size:14px;line-height:1.55;margin-top:6px;width:380px}
.feature:nth-child(even){margin-left:40px}

/* objectives */
.objectives{height:497px;background:var(--orange);color:var(--white);position:relative}
.objectives .sec-head{padding-top:50px}
.objectives .divider i{background:rgba(255,255,255,.7)}
.obj-grid{position:absolute;left:0;top:158px;display:grid;grid-template-columns:repeat(3,333px);text-align:center}
.obj-ring{width:150px;height:150px;border-radius:50%;background:rgba(255,255,255,.25);margin:0 auto;display:flex;align-items:center;justify-content:center}
.obj-ring span{width:124px;height:124px;border-radius:50%;background:#fbe9e2;border:3px solid #f7b9a3;display:flex;align-items:center;justify-content:center}
.obj h3{font-weight:700;font-size:20px;margin-top:22px}
.obj p{font-size:13.5px;line-height:1.5;margin:8px auto 0;width:290px}
.obj-notch{position:absolute;left:50%;bottom:-26px;transform:translateX(-50%)}

/* testimonials */
.testimonials{height:507px;background:var(--grey-bg)}
.testimonials .sec-head{padding-top:70px}
.testimonials h2{color:var(--green)}
.testimonials .divider i{background:var(--green)}
.testimonials .divider b{color:var(--green)}
.quote-card{position:absolute;top:195px;width:455px;height:225px;background:var(--white);box-shadow:0 4px 14px rgba(0,0,0,.12);padding:92px 28px 0}
.quote-card.left{left:0}
.quote-card.right{left:545px}
.avatar{position:absolute;left:28px;top:-32px;width:80px;height:80px;border-radius:50%;border:4px solid var(--white);background:linear-gradient(135deg,#c9a48a,#6e5a4e)}
.right .avatar{background:linear-gradient(135deg,#a5a5a5,#4e4e4e)}
.quote-mark{position:absolute;right:28px;top:36px;color:var(--green);font-family:"Montserrat",sans-serif;font-weight:800;font-size:54px;line-height:1}
.quote-name{position:absolute;left:28px;top:56px;font-size:14px;color:var(--ink)}
.quote-name strong{font-weight:700}
.quote-card p{font-size:13px;line-height:1.6}
.pager{position:absolute;left:50%;transform:translateX(-50%);top:458px;display:flex;gap:14px}
.pager span{width:34px;height:5px;background:#d5d7d9}
.pager span.on{background:var(--orange)}

/* register */
.register{height:418px;position:relative;overflow:hidden}
.register-photo{position:absolute;inset:0;background:linear-gradient(110deg,#2a2a2a 0%,#3b3b3b 40%,#5a5350 65%,#3a3836 100%)}
.register-copy{position:absolute;left:0;top:232px;color:var(--white)}
.register-copy h3{font-weight:700;font-size:26px}
.register-copy h3 span{color:var(--green)}
.register-copy h2{font-weight:800;font-size:68px;color:var(--blue);line-height:1.05;letter-spacing:1px}
.signup{position:absolute;left:636px;top:50px;width:273px;height:315px;background:var(--white);overflow:hidden}
.signup-top{height:120px;background:var(--blue);color:var(--white);text-align:center;font-family:"Montserrat",sans-serif;font-weight:700;font-size:13px;line-height:1.45;padding:20px 20px 0;position:relative}
.signup-top svg{position:absolute;left:0;bottom:-1px}
.signup form{padding:8px 34px 0}
.signup .field{height:30px;border:1px solid #cfe6ef;background:#eaf6fb;margin-bottom:9px;font-size:11px;color:#8a9299;padding:7px 10px}
.signup .submit{height:28px;background:var(--green);color:var(--white);font-family:"Montserrat",sans-serif;font-weight:600;font-size:11px;display:flex;align-items:center;justify-content:center;margin-top:4px}

/* footer */
.footer{height:318px;background:var(--blue);color:var(--white)}
.footer-cols{position:absolute;top:50px;left:0;display:grid;grid-template-columns:335px 227px 235px 203px}
.footer .brand-square{background:var(--green)}
.footer .brand-name{color:var(--white)}
.footer h4{font-weight:700;font-size:17px}
.footer-about h4{margin-top:22px;font-size:15px}
.footer-about p{font-size:11.5px;line-height:1.55;margin-top:6px;width:250px}
.footer ul{list-style:none;margin-top:18px;font-size:12.5px}
.footer ul li{margin-bottom:16px;display:flex;align-items:center;gap:12px}
.footer ul li i{width:22px;height:22px;border-radius:50%;background:var(--white);display:block;flex:none}
.contact-list{margin-top:14px;font-size:12.5px;line-height:1.5}
.contact-list div{display:flex;gap:10px;margin-bottom:10px}
.to-top{position:absolute;right:34px;top:260px;width:48px;height:48px;background:var(--blue-dark);display:flex;align-items:center;justify-content:center}
.copyright{height:53px;background:var(--blue-dark);color:var(--white);font-size:12px;display:flex;align-items:center;justify-content:center;letter-spacing:.8px}
</style>
</head>
<body>

<div class="topbar">
  <div class="container">
    <div class="social-dots"><span></span><span></span><span></span><span></span><span></span></div>
    <div class="top-contact">
      <span><svg width="12" height="12" viewBox="0 0 24 24"><path fill="#fff" d="M6.6 10.8a15 15 0 0 0 6.6 6.6l2.2-2.2a1 1 0 0 1 1-.25 11.4 11.4 0 0 0 3.6.57 1 1 0 0 1 1 1V20a1 1 0 0 1-1 1A17 17 0 0 1 3 4a1 1 0 0 1 1-1h3.5a1 1 0 0 1 1 1c0 1.25.2 2.45.57 3.57a1 1 0 0 1-.25 1z"/></svg>Call us: (555) 310-2040</span>
      <span><svg width="13" height="10" viewBox="0 0 26 20"><rect x="1" y="1" width="24" height="18" fill="none" stroke="#fff" stroke-width="2"/><path d="M1 1l12 10L25 1" fill="none" stroke="#fff" stroke-width="2"/></svg>E-mail: hello@eduvanta-mail.test</span>
    </div>
    <div class="lang">SELECT LANGUAGE &nbsp;▾</div>
  </div>
</div>

<header class="header">
  <div class="container">
    <div class="brand"><span class="brand-square"></span><span class="brand-name">EDUVANTA</span></div>
    <div class="header-info">
      <div>ADDRESS<strong>Northgate 4410</strong></div>
      <div>TIME<strong>MON – SAT: 9:00 – 06:00</strong></div>
    </div>
    <div class="login"><svg width="11" height="13" viewBox="0 0 22 26"><rect x="2" y="11" width="18" height="14" rx="2" fill="#555b61"/><path d="M6 11V7a5 5 0 0 1 10 0v4" fill="none" stroke="#555b61" stroke-width="3"/></svg>Student Login</div>
  </div>
</header>

<nav class="nav">
  <div class="container">
    <ul><li>HOME</li><li>ABOUT US</li><li>ONLINE COURSE</li><li>BLOG</li><li>CONTACT US</li></ul>
    <svg class="search" width="16" height="16" viewBox="0 0 24 24"><circle cx="10" cy="10" r="7" fill="none" stroke="#fff" stroke-width="3"/><path d="M15 15l7 7" stroke="#fff" stroke-width="3"/></svg>
  </div>
</nav>

<section class="hero">
  <div class="hero-photo" role="img" aria-label="Smiling students working together at laptops in a classroom"></div>
  <div class="hero-shade"></div>
  <div class="hero-frame"></div>
  <div class="hero-copy">
    <div class="hero-kicker">EXPLORE ALL OF OUR VACANCIES</div>
    <h1 class="hero-title"><span class="b">LEARN</span> <span class="o">PLAN TEACH</span></h1>
    <p>Get comfortable, confident, and satisfied teaching online with the Ultimate Course Design Program. A comprehensive program for building accredited online cources.</p>
    <a class="btn">GET STARTED <svg width="14" height="10" viewBox="0 0 14 10"><path d="M0 5h12M8 1l4 4-4 4" fill="none" stroke="#fff" stroke-width="1.6"/></svg></a>
  </div>
  <div class="hero-dots">
    <span><svg width="8" height="10" viewBox="0 0 8 10"><path d="M6 1L2 5l4 4" fill="none" stroke="#333" stroke-width="1.6"/></svg></span>
    <span class="on"><svg width="8" height="10" viewBox="0 0 8 10"><path d="M2 1l4 4-4 4" fill="none" stroke="#fff" stroke-width="1.6"/></svg></span>
  </div>
  <svg class="hero-notch" width="90" height="26" viewBox="0 0 90 26"><path d="M0 26C22 26 26 0 45 0s23 26 45 26z" fill="#fff"/><path d="M39 10l6 6 6-6" fill="none" stroke="#8dc63f" stroke-width="2"/></svg>
</section>

<section class="intro">
  <div class="container">
    <div class="welcome"><span>WELCOME</span><i></i></div>
    <h2 class="intro-title">THE ULTIMATE<br>COURSE DESIGN PROGRAM</h2>
    <div class="intro-sub">A Practical, Comprehensive Approach that Gets You Ahead</div>
    <p class="intro-text">The Ultimate Course Design Program will teach you an organized and practical approach to creating accreditable courses that are visually appealing, engaging and highly interactive. Through this virtual program with LIVE weekly meetings and virtual one-on-one meetings, you will become more comfortable and satisfied with what you design, how you create it, and best of all, how you teach.</p>
    <div class="intro-actions">
      <a class="btn">GET STARTED <svg width="14" height="10" viewBox="0 0 14 10"><path d="M0 5h12M8 1l4 4-4 4" fill="none" stroke="#fff" stroke-width="1.6"/></svg></a>
      <div class="phone"><i><svg width="18" height="18" viewBox="0 0 24 24"><path fill="#fff" d="M6.6 10.8a15 15 0 0 0 6.6 6.6l2.2-2.2a1 1 0 0 1 1-.25 11.4 11.4 0 0 0 3.6.57 1 1 0 0 1 1 1V20a1 1 0 0 1-1 1A17 17 0 0 1 3 4a1 1 0 0 1 1-1h3.5a1 1 0 0 1 1 1c0 1.25.2 2.45.57 3.57a1 1 0 0 1-.25 1z"/></svg></i>(555) 310 2041</div>
    </div>
    <div class="intro-media" role="img" aria-label="Grid of four black and white photos of students studying in class">
      <div></div><div></div><div></div><div></div>
    </div>
    <div class="video-box">
      <svg width="34" height="26" viewBox="0 0 34 26"><rect x="1" y="1" width="32" height="24" rx="3" fill="none" stroke="#f15a2b" stroke-width="2"/><path d="M14 8v10l8-5z" fill="#f15a2b"/></svg>
      Video About Us
    </div>
  </div>
</section>

<section class="features">
  <div class="container">
    <div class="sec-head">
      <h2>THE ULTIMATE COURSE DESIGN PROGRAM FEATURES</h2>
      <p>A Collaborative Approach to Creating Accreditable Online Courses</p>
      <div class="divider"><i></i><b>★★★</b><i></i></div>
    </div>
    <div class="feature-grid">
      <div class="feature">
        <div class="f-icon" style="background:var(--orange)"><svg width="44" height="40" viewBox="0 0 44 40"><rect x="3" y="3" width="32" height="22" fill="none" stroke="#fff" stroke-width="2.5"/><path d="M10 32l9-7 9 7" fill="none" stroke="#fff" stroke-width="2.5"/><circle cx="34" cy="28" r="6" fill="none" stroke="#fff" stroke-width="2.5"/><path d="M38 32l4 5" stroke="#fff" stroke-width="2.5"/></svg></div>
        <div><h3>EFFECTIVE LESSONS</h3><p>All Lessons has been designed by experienced instructors with interactive teaching techniques will help students to achieve course excellence.</p></div>
      </div>
      <div class="feature">
        <div class="f-icon" style="background:var(--blue)"><svg width="36" height="40" viewBox="0 0 36 40"><rect x="3" y="3" width="30" height="34" fill="none" stroke="#fff" stroke-width="2.5"/><path d="M9 12h4M17 12h10M9 20h4M17 20h10M9 28h4M17 28h10" stroke="#fff" stroke-width="2.5"/></svg></div>
        <div><h3>AWESOME QUIZZES</h3><p>So many amazing questions types provide entertaining and informative quizzes help prepare students for the course assesments.</p></div>
      </div>
      <div class="feature">
        <div class="f-icon" style="background:var(--green)"><svg width="44" height="36" viewBox="0 0 44 36"><rect x="3" y="3" width="38" height="30" fill="none" stroke="#fff" stroke-width="2.5"/><path d="M3 10h38" stroke="#fff" stroke-width="2.5"/><path d="M18 15v12l10-6z" fill="#fff"/></svg></div>
        <div><h3>QUALITY VIDEOS</h3><p>Save time and money by uploading video content directly to Eduvanta Studio. We handle all of your video hosting and streaming needs.</p></div>
      </div>
      <div class="feature">
        <div class="f-icon" style="background:var(--navy)"><svg width="40" height="36" viewBox="0 0 40 36"><rect x="3" y="3" width="34" height="30" fill="none" stroke="#fff" stroke-width="2.5"/><path d="M3 10h34" stroke="#fff" stroke-width="2.5"/><rect x="9" y="15" width="10" height="12" fill="none" stroke="#fff" stroke-width="2"/><path d="M23 17h8M23 22h8M23 27h6" stroke="#fff" stroke-width="2"/></svg></div>
        <div><h3>HOSTED CONTENT</h3><p>Upload documents, presentations, images, and resources. Simply drag and drop content from your computer straight into the course.</p></div>
      </div>
    </div>
  </div>
</section>

<section class="objectives">
  <div class="container">
    <div class="sec-head">
      <h2>LEARNING OBJECTIVES</h2>
      <p>So many academic goals that we expect you to achieve</p>
      <div class="divider"><i></i><b>★★★</b><i></i></div>
    </div>
    <div class="obj-grid">
      <div class="obj">
        <div class="obj-ring"><span><svg width="56" height="56" viewBox="0 0 56 56"><path d="M18 50V40c-6-4-9-10-9-17A19 19 0 0 1 47 22l4 8h-5v8a4 4 0 0 1-4 4h-6v8" fill="none" stroke="#8dc63f" stroke-width="2.5"/><circle cx="29" cy="22" r="6" fill="none" stroke="#8dc63f" stroke-width="2.5"/></svg></span></div>
        <h3>SKILL</h3>
        <p>Lorem Ipsum is simply dummy text of the printing and typesetting industry. Lorem Ipsum has been the industry's standard dummy text ever since the 1500s</p>
      </div>
      <div class="obj">
        <div class="obj-ring"><span><svg width="58" height="52" viewBox="0 0 58 52"><path d="M3 16L29 5l26 11-26 11z" fill="none" stroke="#8dc63f" stroke-width="2.5"/><path d="M13 21v12c8 6 24 6 32 0V21" fill="none" stroke="#8dc63f" stroke-width="2.5"/><path d="M51 18v14" stroke="#8dc63f" stroke-width="2.5"/><rect x="22" y="34" width="14" height="14" fill="none" stroke="#8dc63f" stroke-width="2.5"/></svg></span></div>
        <h3>SELF LEARNING</h3>
        <p>Lorem Ipsum is simply dummy text of the printing and typesetting industry. Lorem Ipsum has been the industry's standard dummy text ever since the 1500s</p>
      </div>
      <div class="obj">
        <div class="obj-ring"><span><svg width="58" height="52" viewBox="0 0 58 52"><path d="M3 16L29 5l26 11-26 11z" fill="none" stroke="#8dc63f" stroke-width="2.5"/><path d="M13 21v12c8 6 24 6 32 0V21" fill="none" stroke="#8dc63f" stroke-width="2.5"/><path d="M51 18v14" stroke="#8dc63f" stroke-width="2.5"/><rect x="22" y="34" width="14" height="14" fill="none" stroke="#8dc63f" stroke-width="2.5"/></svg></span></div>
        <h3>SELF LEARNING</h3>
        <p>Lorem Ipsum is simply dummy text of the printing and typesetting industry. Lorem Ipsum has been the industry's standard dummy text ever since the 1500s</p>
      </div>
    </div>
  </div>
  <svg class="obj-notch" width="70" height="28" viewBox="0 0 70 28"><path d="M0 0h70C52 0 46 28 35 28S18 0 0 0z" fill="#f15a2b"/><circle cx="35" cy="10" r="3" fill="#fff"/></svg>
</section>

<section class="testimonials">
  <div class="container">
    <div class="sec-head">
      <h2>WHAT PEOPLE ARE SAYING</h2>
      <div class="divider"><i></i><b>★★★</b><i></i></div>
    </div>
    <div class="quote-card left">
      <div class="avatar" role="img" aria-label="Portrait photo of Mira Castell"></div>
      <div class="quote-name"><strong>Mira Castell</strong> / CEO</div>
      <div class="quote-mark">”</div>
      <p>Lorem Ipsum is simply dummy text of the printing and typesetting industry. Lorem Ipsum has been the industry's standard dummy text ever since the 1500s, when an unknown printer took a galley of type and scrambled it to make a type specimen book.</p>
    </div>
    <div class="quote-card right">
      <div class="avatar" role="img" aria-label="Portrait photo of Tomas Reyne"></div>
      <div class="quote-name"><strong>Tomas Reyne</strong> / Manager</div>
      <div class="quote-mark">”</div>
      <p>Lorem Ipsum is simply dummy text of the printing and typesetting industry. Lorem Ipsum has been the industry's standard dummy text ever since the 1500s, when an unknown printer took a galley of type and scrambled it to make a type specimen book.</p>
    </div>
    <div class="pager"><span class="on"></span><span></span><span></span></div>
  </div>
</section>

<section class="register">
  <div class="register-photo" role="img" aria-label="Dimmed photo of students learning together at computers"></div>
  <div class="container">
    <div class="register-copy">
      <h3>GET 100S OF ONLINE <span>COURSES FOR FREE</span></h3>
      <h2>REGISTER NOW</h2>
    </div>
    <div class="signup">
      <div class="signup-top">Create your free account now and get immediate access to 100s of online courses
        <svg width="273" height="34" viewBox="0 0 273 34" preserveAspectRatio="none"><path d="M0 34V0c60 30 213 30 273 0v34z" fill="#fff"/></svg>
      </div>
      <form>
        <div class="field">Name</div>
        <div class="field">Email</div>
        <div class="field">Phone</div>
        <div class="submit">GET IT NOW</div>
      </form>
    </div>
  </div>
</section>

<footer class="footer">
  <div class="container">
    <div class="footer-cols">
      <div class="footer-about">
        <div class="brand"><span class="brand-square"></span><span class="brand-name">EDUVANTA</span></div>
        <h4>About us</h4>
        <p>Lorem Ipsum is simply dummy text of the printing and typesetting industry. Lorem Ipsum has been the industry's standard dummy text ever since the 1500s, when an unknown printer took a galley of type and scrambled it to make a type specimen book. It has survived not only five centuries, but also the leap into electronic typesetting, remaining essentially unchanged.</p>
      </div>
      <div>
        <h4>Quick Link</h4>
        <ul><li>Home</li><li>About Us</li><li>Online Course</li><li>Blog</li><li>Contact us</li></ul>
      </div>
      <div>
        <h4>Follow us</h4>
        <ul><li><i></i>Friendbook</li><li><i></i>Chirper</li><li><i></i>Circlespace</li><li><i></i>WorkLink</li><li><i></i>ViewTube</li></ul>
      </div>
      <div>
        <h4>Contact Us</h4>
        <div class="contact-list">
          <div>EDUVANTA EDUCATION</div>
          <div><svg width="10" height="14" viewBox="0 0 20 28"><path d="M10 0a10 10 0 0 0-10 10c0 8 10 18 10 18s10-10 10-18A10 10 0 0 0 10 0z" fill="#fff"/><circle cx="10" cy="10" r="4" fill="#1b9bd7"/></svg><span>Northgate District 4410<br>18 Larchfield Road<br>Westbay</span></div>
          <div><svg width="12" height="12" viewBox="0 0 24 24"><path fill="#fff" d="M6.6 10.8a15 15 0 0 0 6.6 6.6l2.2-2.2a1 1 0 0 1 1-.25 11.4 11.4 0 0 0 3.6.57 1 1 0 0 1 1 1V20a1 1 0 0 1-1 1A17 17 0 0 1 3 4a1 1 0 0 1 1-1h3.5a1 1 0 0 1 1 1c0 1.25.2 2.45.57 3.57a1 1 0 0 1-.25 1z"/></svg><span>(555) 310 - 2040<br>(555) 310 - 2042</span></div>
          <div><svg width="13" height="10" viewBox="0 0 26 20"><rect x="1" y="1" width="24" height="18" fill="none" stroke="#fff" stroke-width="2"/><path d="M1 1l12 10L25 1" fill="none" stroke="#fff" stroke-width="2"/></svg><span>hello@eduvanta-mail.test</span></div>
        </div>
      </div>
    </div>
    <div class="to-top"><svg width="16" height="16" viewBox="0 0 16 16"><path d="M3 8l5-5 5 5M3 13l5-5 5 5" fill="none" stroke="#fff" stroke-width="2"/></svg></div>
  </div>
</footer>
<div class="copyright">COPYRIGHT © 2018, EDUVANTA EDUCATION. ALL RIGHTS RESERVED</div>

</body>
</html>
```